Professional educational and informative brochures for CPAP alternative treatment for sleep apnea

I am a dentist who practices dental sleep medicine, alternative to CPAP, such as custom-fit oral appliance therapy, laser treatment, and other adjunctive treatments. I need a professional trifold brochure to give directly to patients and physicians. The brochure needs to be educational and informative, and I would also like it to provide some information about me from a marketing standpoint. I had a custom brochure made in the past, more catered for patients, but it looks too crowded with info and hard to read. I need a clean and easy-to-read brochure. It could be tri-fold or quarter-fold. I attached some files on my current brochure, business card, and logos for your review and ideas.
Updates

Nothing really caught my attention. Plus most of them are out of target of what I am looking for. I put more specific info on my project.

Target Market(s)

Referring physicians and self referred patients who seeks CPAP alternative treatments

Industry/Entity Type

Healthcare

Requirements
Must have
• a message that emphasizes that I can provide treatments alternative to CPAP for sleep apnea patients who do not tolerate CPAP
Nice to have
• pictures of each treatments I provide instead of CPAP
Should not have
• a message that confuses people that I am promoting CPAP as a CPAP provider because I am not!

```html
<!DOCTYPE html>
<html lang="en">
<head>
<meta charset="utf-8">
<title>Starlit Rest Dental – Sleep Apnea Brochure</title>
<link href="https://fonts.googleapis.com/css2?family=Montserrat:wght@300;400;600;700;800&family=Lora:wght@400&family=Open+Sans:wght@400&display=swap" rel="stylesheet">
<style>
  :root{
    --navy:#141c33;
    --navy-soft:#3d4862;
    --gold:#e3a81c;
    --gold-deep:#c98f12;
    --ink:#2a2a2a;
    --grey-band:#b9bcc6;
    --paper:#ffffff;
    --pale:#eceef2;
  }
  *{box-sizing:border-box;margin:0;padding:0}
  html,body{width:835px;height:1200px;overflow:hidden;background:var(--paper)}
  body{position:relative;font-family:'Open Sans',sans-serif;color:var(--ink)}
  .spread{position:absolute;left:59px;width:690px;height:488px;overflow:hidden;box-shadow:0 1px 3px rgba(0,0,0,.25);background:var(--paper)}
  .spread--outside{top:63px}
  .spread--inside{top:609px}
  .spread svg.backdrop{position:absolute;left:0;top:0;width:690px;height:488px}
  .abs{position:absolute}
  .eyebrow{font-family:'Montserrat',sans-serif;font-weight:300;color:var(--navy);letter-spacing:.5px}
  .headline{font-family:'Montserrat',sans-serif;font-weight:800;color:var(--navy)}
  .rule{position:absolute;height:3px;background:var(--gold)}
  .serif-body{font-family:'Lora',serif;font-size:7.4px;line-height:11.8px;color:#333}
  .signs-text{font-family:'Montserrat',sans-serif;font-weight:800;color:#fff;font-size:13.5px;line-height:18.8px;text-align:center;width:160px}
  .contact-title{font-family:'Montserrat',sans-serif;font-weight:800;color:var(--gold);font-size:19px;width:230px;text-align:center}
  .contact-line{font-family:'Montserrat',sans-serif;color:#fff;width:230px;text-align:center}
  .brand-name{font-family:'Montserrat',sans-serif;font-weight:400;color:#fff;font-size:13px;line-height:15px;text-align:center;width:140px}
  .doctor-tag{background:var(--navy);color:#fff;font-family:'Montserrat',sans-serif;font-weight:800;font-size:12.5px;display:flex;align-items:center;justify-content:center}
  .invest-title{font-family:'Montserrat',sans-serif;font-weight:800;color:var(--navy);font-size:13.5px;line-height:19px;text-align:center;width:200px}
  .invest-body{font-size:9.4px;line-height:15.7px;text-align:center;width:210px;color:#222}
  .panel-title{font-family:'Montserrat',sans-serif;font-weight:800;font-size:14.8px;line-height:21.5px;letter-spacing:.3px}
  .benefit{position:absolute;left:14px;display:flex;align-items:center;width:210px}
  .benefit-icon{flex:none;width:28px;height:28px;border-radius:50%;background:var(--gold);display:flex;align-items:center;justify-content:center;margin-right:8px}
  .benefit-text{color:#fff;font-size:9.6px;line-height:14px}
  .fact{position:absolute;left:16px;width:205px;font-size:10.2px;line-height:17.8px;color:#222;padding-left:11px}
  .fact::before{content:"";position:absolute;left:0;top:6px;width:6px;height:6px;border-radius:50%;background:var(--navy)}
</style>
</head>
<body>

<!-- Outside spread -->
<section class="spread spread--outside">
  <svg class="backdrop" viewBox="0 0 690 488">
    <defs>
      <linearGradient id="coupleTone" x1="0" y1="0" x2="1" y2="1">
        <stop offset="0" stop-color="#8a6a1c"/><stop offset=".5" stop-color="#c9a23a"/><stop offset="1" stop-color="#6e5316"/>
      </linearGradient>
      <linearGradient id="maskTone" x1="0" y1="0" x2="1" y2="1">
        <stop offset="0" stop-color="#b8962e"/><stop offset="1" stop-color="#4f3c12"/>
      </linearGradient>
    </defs>
    <!-- left panel stripes -->
    <polygon points="22,0 230,0 230,135" fill="var(--navy)"/>
    <polygon points="0,0 22,0 230,135 230,160 0,28" fill="var(--gold)"/>
    <!-- middle panel -->
    <rect x="230" y="0" width="230" height="488" fill="var(--navy)"/>
    <!-- couple photo -->
    <path role="img" aria-label="Photo: woman kept awake by her partner snoring in bed" d="M230,0 L690,0 L690,213 L565,288 Q537,302 505,288 L459,271 L230,137 Z" fill="url(#coupleTone)"/>
    <!-- logo disc -->
    <circle cx="544" cy="3" r="84" fill="var(--gold)"/>
    <!-- signs badge -->
    <circle cx="345" cy="218" r="77" fill="var(--gold)"/>
    <circle cx="345" cy="218" r="71" fill="none" stroke="#fff" stroke-width="1.2"/>
    <!-- mask photo -->
    <path role="img" aria-label="Photo: woman sleeping with an oral CPAP mask" d="M0,322 L40,343 C90,318 160,322 205,372 L240,425 L290,488 L0,488 Z" fill="url(#maskTone)"/>
  </svg>

  <p class="abs eyebrow" style="left:31px;top:122px;font-size:17px">WHAT IS</p>
  <h2 class="abs headline" style="left:31px;top:145px;font-size:18px">SLEEP APNEA?</h2>
  <div class="rule" style="left:31px;top:176px;width:58px"></div>
  <p class="abs serif-body" style="left:31px;top:187px;width:190px">Sleep apnea is a serious sleep disorder in which breathing repeatedly stops while you sleep. It happens when your throat and tongue muscles relax and closing your airway preventing you from getting air when you sleep.</p>
  <p class="abs serif-body" style="left:31px;top:258px;width:190px">Snoring is common and can be a first sign of sleep apnea. If it is untreated, it can develop into sleep apnea. Your snoring affects not only the relationship with your bed partner but also his/her sleep quality which results in poor health.</p>

  <p class="abs brand-name" style="left:474px;top:42px">Starlit Rest<br>Dental</p>

  <p class="abs signs-text" style="left:265px;top:170px">SIGNS<br>YOU MAY<br>NOT KNOW<br>YOU HAVE<br>SLEEP APNEA</p>

  <h3 class="abs contact-title" style="left:230px;top:309px">CONTACT US</h3>
  <p class="abs contact-line" style="left:230px;top:397px;font-size:11px;font-weight:700">STARLIT REST DENTAL</p>
  <p class="abs contact-line" style="left:230px;top:422px;font-size:11.5px;font-weight:700">(555) 010-2874</p>
  <p class="abs contact-line" style="left:230px;top:447px;font-size:9.8px;font-weight:400">www.StarlitRestDental.com</p>

  <p class="abs eyebrow" style="left:488px;top:326px;font-size:21px">DO YOU HAVE</p>
  <h2 class="abs headline" style="left:487px;top:354px;font-size:22px">SLEEP APNEA?</h2>
  <div class="rule" style="left:488px;top:390px;width:54px"></div>
  <p class="abs serif-body" style="left:488px;top:402px;width:180px">Sleep apnea is a serious sleep disorder in which breathing repeatedly stops while you sleep. It happens when your throat and tongue muscles relax and closing your airway preventing you from getting air when you sleep.</p>
</section>

<!-- Inside spread -->
<section class="spread spread--inside">
  <svg class="backdrop" viewBox="0 0 690 488">
    <defs>
      <linearGradient id="doctorTone" x1="0" y1="0" x2="1" y2="1">
        <stop offset="0" stop-color="#d9dde0"/><stop offset=".6" stop-color="#7a7a7a"/><stop offset="1" stop-color="#c7cacd"/>
      </linearGradient>
      <linearGradient id="smileTone" x1="0" y1="0" x2="1" y2="1">
        <stop offset="0" stop-color="#9fb0bf"/><stop offset=".6" stop-color="#e0c2a4"/><stop offset="1" stop-color="#a07a52"/>
      </linearGradient>
    </defs>
    <!-- left panel -->
    <rect x="0" y="0" width="230" height="488" fill="var(--pale)"/>
    <polygon points="0,195 230,340 230,488 0,488" fill="#fff"/>
    <path d="M0,0 L230,0 L230,95 C225,155 175,189 115,189 C60,189 8,160 0,120 Z" fill="var(--gold)"/>
    <path role="img" aria-label="Photo: portrait of the dentist smiling in a white coat" d="M0,0 L230,0 L230,88 C220,145 172,178 115,178 C62,178 12,150 0,112 Z" fill="url(#doctorTone)"/>
    <!-- middle panel -->
    <rect x="230" y="0" width="230" height="488" fill="var(--navy)"/>
    <polygon points="230,113 459,239 459,488 230,488" fill="var(--navy-soft)"/>
    <!-- right panel -->
    <rect x="460" y="0" width="230" height="488" fill="var(--grey-band)"/>
    <polygon points="468,0 690,0 690,133" fill="#fff"/>
    <polygon points="460,250 600,340 460,340" fill="#fff"/>
    <path d="M460,488 L460,418 C460,355 512,306 578,306 C630,306 672,333 690,366 L690,488 Z" fill="var(--gold)"/>
    <path role="img" aria-label="Photo: smiling patient in a dental chair" d="M464,488 L464,420 C464,360 516,315 578,315 C628,315 668,340 690,372 L690,488 Z" fill="url(#smileTone)"/>
    <!-- membership badges as plain shapes -->
    <circle cx="51" cy="451" r="16" fill="none" stroke="var(--navy)" stroke-width="2.5"/>
    <rect x="77" y="440" width="45" height="22" rx="2" fill="#c9ccd4"/>
    <rect x="140" y="437" width="54" height="28" fill="none" stroke="#c9ccd4" stroke-width="1.5"/>
  </svg>

  <div class="abs doctor-tag" style="left:29px;top:202px;width:172px;height:28px">DANA HOSHINO, DMD</div>
  <h3 class="abs invest-title" style="left:15px;top:239px">INVEST IN YOUR HEALTH AND GET A GOOD NIGHT REST</h3>
  <p class="abs invest-body" style="left:10px;top:297px">Sleep apnea is closely linked to several life-threatening conditions, and it could shorten your life span from anywhere between 12-15 years. Treating sleep apnea will improve the quality of life and even help save life.<br>Dr. Dana and her team believe you deserve a good night's sleep.</p>

  <div class="abs" style="left:230px;top:0;width:230px;height:488px">
    <h3 class="abs panel-title" style="left:14px;top:15px;color:#fff">BENEFITS OF ORAL<br>APPLIANCES OVER CPAP</h3>
    <div class="rule" style="left:14px;top:68px;width:50px"></div>

    <div class="benefit" style="top:84px"><span class="benefit-icon"><svg width="14" height="14" viewBox="0 0 14 14"><path d="M2,7 L6,11 L12,3" stroke="#fff" stroke-width="1.6" fill="none"/></svg></span><span class="benefit-text">More comfortable to wear than CPAP</span></div>
    <div class="benefit" style="top:119px"><span class="benefit-icon"><svg width="14" height="14" viewBox="0 0 14 14"><circle cx="5" cy="9" r="3" fill="none" stroke="#fff" stroke-width="1.2"/><circle cx="10" cy="5" r="2" fill="none" stroke="#fff" stroke-width="1.2"/></svg></span><span class="benefit-text">Easier to clean</span></div>
    <div class="benefit" style="top:155px"><span class="benefit-icon"><svg width="14" height="14" viewBox="0 0 14 14"><rect x="2" y="4" width="10" height="8" rx="1" fill="none" stroke="#fff" stroke-width="1.2"/><path d="M5,4 V2 H9 V4" fill="none" stroke="#fff" stroke-width="1.2"/></svg></span><span class="benefit-text">Easier to travel as it is very compact</span></div>
    <div class="benefit" style="top:196px"><span class="benefit-icon"><svg width="14" height="14" viewBox="0 0 14 14"><circle cx="7" cy="7" r="4" fill="none" stroke="#fff" stroke-width="1.4"/><circle cx="7" cy="7" r="1.3" fill="#fff"/></svg></span><span class="benefit-text">Quiet as there is no machine next to you</span></div>
    <div class="benefit" style="top:239px"><span class="benefit-icon"><svg width="14" height="14" viewBox="0 0 14 14"><ellipse cx="7" cy="7" rx="5" ry="3.5" fill="none" stroke="#fff" stroke-width="1.3"/></svg></span><span class="benefit-text">No dry mouth, throat or nose</span></div>
    <div class="benefit" style="top:282px"><span class="benefit-icon"><svg width="14" height="14" viewBox="0 0 14 14"><path d="M3,11 V5 H8 V2 M8,5 H11 V11" fill="none" stroke="#fff" stroke-width="1.3"/></svg></span><span class="benefit-text">No bloating or gas from the air pressure</span></div>
    <div class="benefit" style="top:326px"><span class="benefit-icon"><svg width="14" height="14" viewBox="0 0 14 14"><rect x="2" y="3" width="10" height="9" fill="none" stroke="#fff" stroke-width="1.2"/><path d="M2,6 H12" stroke="#fff" stroke-width="1.2"/></svg></span><span class="benefit-text">No monthly maintenance and costs to</span></div>
    <div class="benefit" style="top:363px"><span class="benefit-icon"><svg width="14" height="14" viewBox="0 0 14 14"><circle cx="7" cy="7" r="5" fill="none" stroke="#fff" stroke-width="1.2"/><path d="M4.5,8.5 Q7,10.5 9.5,8.5" fill="none" stroke="#fff" stroke-width="1.2"/></svg></span><span class="benefit-text">change hoses and face mask</span></div>
    <div class="benefit" style="top:400px;align-items:flex-start"><span class="benefit-icon"><svg width="14" height="14" viewBox="0 0 14 14"><path d="M7,2 L8.5,5.5 L12,6 L9.5,8.5 L10,12 L7,10.3 L4,12 L4.5,8.5 L2,6 L5.5,5.5 Z" fill="none" stroke="#fff" stroke-width="1.1"/></svg></span><span class="benefit-text">Looks much sexier than wearing CPAP<br><i>(No one wants to look like a space villain in bed)</i></span></div>
  </div>

  <div class="abs" style="left:460px;top:0;width:230px;height:488px">
    <h3 class="abs panel-title" style="left:16px;top:15px;color:var(--navy)">BENEFITS OF ORAL<br>APPLIANCES OVER CPAP</h3>
    <div class="rule" style="left:16px;top:68px;width:50px"></div>
    <p class="fact" style="top:80px">A 2022 study found that Oral Appliances can be 94% effective in treating mild to moderate sleep apnea.</p>
    <p class="fact" style="top:152px">Oral Appliances were 81% successful across all levels of sleep apnea severity in reducing snore and improving the sleep quality and energy level.</p>
    <p class="fact" style="top:241px">A 2022 study found that Oral Appliances can be 94% effective in treating mild to moderate sleep apnea.</p>
  </div>
</section>

</body>
</html>
```